Ad for new Australian trade product

We need an A4 point of sale advertisement for a new product called the TWIST HOOK Silicone Nozzle to go on the counter of retail outlets. The design should be clean, with a focus on blues or the colours used in our logo. We need to have photos of our product included as well as some features/benefits. Our products is aimed at plumbers and trades people.
Updates

Size for ad is A4. The photos loaded are the only ones available.

Thank you 

Thank you to everyone for their very creative visions with our product. We appreciate the prompt responses that we have had and the professionalism of all. Thanks again

Target Market(s)

plumbers, tradesmen

Industry/Entity Type

Retail

Requirements
Must have
• 2 photos we have attached
the two logos that we have attached
Text of attached word file, please disgard font used in file.
no changes to the Harbour Crafted logo
no changes to the TWIST HOOK logo (can remove white background)
$8.75 inc GST
Nice to have
• - either a block of colour at the top or bottom of the page that - curves up
- symbol or sign that indicates that it is a new/available now product
-background can be removed from pictures/ or pictures should have borders etc around them
-Harbour Crafted logo to be smaller than TWIST HOOK Logo
Should not have
• - no cartoons
- no old style-style fonts

```html
<!DOCTYPE html>
<html lang="en">
<head>
<meta charset="utf-8">
<title>TWIST HOOK Silicone Nozzles – Counter Ad</title>
<link href="https://fonts.googleapis.com/css2?family=Oswald:wght@500;700&family=Archivo+Narrow:wght@700&display=swap" rel="stylesheet">
<style>
  :root {
    --steel-light: #d9d9d9;
    --steel-mid: #a8a8a8;
    --steel-dark: #6e6e6e;
    --panel-top: #141414;
    --panel-mid: #5a5a5a;
    --panel-floor: #f2f2f2;
    --ink: #0b0b0b;
    --white: #ffffff;
    --feature-green: #4fd14a;
    --gold-light: #e8e2a6;
    --gold: #c9bf6c;
    --gold-dark: #8d8440;
    --brand-navy: #1f2a78;
    --brand-grey: #7a7a7a;
    --badge-green: #007a3d;
  }
  * { box-sizing: border-box; margin: 0; padding: 0; }
  html, body { width: 849px; height: 1200px; overflow: hidden; background: var(--steel-mid); }
  .ad {
    position: relative; width: 849px; height: 1200px; overflow: hidden;
    background:
      repeating-linear-gradient(120deg, rgba(255,255,255,.18) 0 2px, rgba(0,0,0,.06) 2px 5px),
      linear-gradient(135deg, var(--steel-light), var(--steel-mid) 40%, var(--steel-light) 70%, var(--steel-dark));
  }
  .panel {
    position: absolute; left: 31px; top: 31px; width: 787px; height: 1138px;
    background: linear-gradient(180deg, var(--panel-top) 0%, #2d2d2d 25%, var(--panel-mid) 50%, #bdbdbd 70%, var(--panel-floor) 78%, #e4e4e4 100%);
    box-shadow: 0 0 18px rgba(0,0,0,.6);
  }
  .headline {
    position: absolute; left: 0; top: 56px; width: 100%;
    text-align: center; font-family: "Oswald", sans-serif; font-weight: 700;
    font-size: 61px; line-height: 1.2; letter-spacing: 1px; text-transform: uppercase;
    color: var(--white);
    background: linear-gradient(180deg, #ffffff 0%, #f0f0f0 55%, #b9b9b9 100%);
    -webkit-background-clip: text; background-clip: text; -webkit-text-fill-color: transparent;
    filter: drop-shadow(0 3px 3px rgba(0,0,0,.8));
  }
  .rule {
    position: absolute; left: 212px; top: 306px; width: 386px; height: 4px;
    background: linear-gradient(90deg, #9a9a9a, #e0e0e0, #9a9a9a);
  }
  .product-photo {
    position: absolute; left: 283px; top: 332px; width: 310px; height: 600px;
    background: radial-gradient(ellipse at 50% 50%, #2a2a2a 0%, #111 35%, rgba(17,17,17,0) 70%);
  }
  .callouts { position: absolute; left: 0; top: 0; width: 787px; height: 1138px; }
  .feature {
    position: absolute; left: 95px; width: 238px; padding: 6px 8px 7px;
    background: var(--ink); border: 1px solid #333; text-align: center;
  }
  .feature h2 {
    font-family: "Archivo Narrow", sans-serif; font-weight: 700; font-size: 19px;
    color: var(--feature-green); letter-spacing: 1px; line-height: 1.1;
  }
  .feature p {
    font-family: "Archivo Narrow", sans-serif; font-weight: 700; font-size: 9.5px;
    color: var(--white); line-height: 1.35; text-transform: uppercase; margin-top: 2px;
  }
  .feature--flexible { top: 411px; }
  .feature--extendable { top: 523px; }
  .feature--reusable { top: 637px; }
  .price-tag { position: absolute; left: -31px; top: 779px; width: 400px; height: 150px; }
  .price-tag svg { position: absolute; inset: 0; }
  .price-lead {
    position: absolute; left: 38px; top: 22px;
    font-family: "Oswald", sans-serif; font-weight: 500; font-size: 25px; color: var(--ink);
  }
  .price-amount {
    position: absolute; left: 36px; top: 44px;
    font-family: "Oswald", sans-serif; font-weight: 700; font-size: 82px; line-height: 1; color: var(--ink);
    letter-spacing: -1px;
  }
  .price-amount small { font-size: 20px; font-weight: 700; letter-spacing: 0; margin-left: 4px; }
  .origin-badge { position: absolute; left: 33px; top: 984px; width: 120px; text-align: center; }
  .origin-badge .mark { width: 64px; height: 64px; margin: 0 auto 4px; background: var(--badge-green); }
  .origin-badge span {
    font-family: "Archivo Narrow", sans-serif; font-weight: 700; font-size: 10px;
    color: var(--ink); text-transform: uppercase;
  }
  .tagline {
    position: absolute; left: 180px; top: 1012px; width: 300px; text-align: center;
    font-family: "Archivo Narrow", sans-serif; font-weight: 700; font-size: 15px;
    color: var(--ink); text-transform: uppercase;
  }
  .brand { position: absolute; left: 530px; top: 880px; width: 240px; text-align: center; }
  .brand .mark {
    width: 150px; height: 150px; margin: 0 auto 8px; border-radius: 50%;
    border: 8px solid var(--brand-navy); background: #fafafa;
  }
  .brand-name {
    font-family: "Oswald", sans-serif; font-weight: 700; font-size: 30px;
    color: var(--brand-navy); line-height: 1; letter-spacing: 1px;
  }
  .brand-sub {
    font-family: "Archivo Narrow", sans-serif; font-weight: 700; font-size: 14px;
    color: var(--brand-grey); margin-top: 3px;
  }
</style>
</head>
<body>
<main class="ad">
  <section class="panel">
    <h1 class="headline">Increase efficiency, saving<br>yourself time, money<br>and wastage</h1>
    <div class="rule"></div>

    <div class="product-photo" role="img" aria-label="Photo of the black jointed silicone nozzle standing upright, bent through several ball joints"></div>

    <svg class="callouts" viewBox="0 0 787 1138" aria-hidden="true">
      <polygon points="333,430 333,458 347,556" fill="#0b0b0b"/>
      <polygon points="333,546 333,572 349,556" fill="#0b0b0b"/>
      <polygon points="333,656 333,684 347,560" fill="#0b0b0b"/>
    </svg>

    <div class="feature feature--flexible">
      <h2>FLEXIBLE</h2>
      <p>Features ball joints<br>that pivot to all angles</p>
    </div>
    <div class="feature feature--extendable">
      <h2>EXTENDABLE</h2>
      <p>Adding additional ball joints<br>gets you into all those hard<br>to reach places</p>
    </div>
    <div class="feature feature--reusable">
      <h2>REUSABLE</h2>
      <p>Internal smoothness, for<br>effortless transfer of<br>sealant and non-stick removal</p>
    </div>

    <div class="price-tag">
      <svg viewBox="0 0 400 150" aria-hidden="true">
        <defs>
          <linearGradient id="tagGold" x1="0" y1="0" x2="0" y2="1">
            <stop offset="0" stop-color="#e8e2a6"/>
            <stop offset=".5" stop-color="#c9bf6c"/>
            <stop offset="1" stop-color="#a79d4c"/>
          </linearGradient>
        </defs>
        <polygon points="0,6 320,6 396,75 320,144 0,144" fill="url(#tagGold)" stroke="#8d8440" stroke-width="3"/>
        <polygon points="8,14 316,14 384,75 316,136 8,136" fill="none" stroke="#f6f1c8" stroke-width="1.5" stroke-dasharray="5 4"/>
        <circle cx="336" cy="75" r="9" fill="#5a5a5a" stroke="#8d8440" stroke-width="2"/>
      </svg>
      <div class="price-lead">FOR ONLY</div>
      <div class="price-amount">$8.75<small>INC GST</small></div>
    </div>

    <div class="origin-badge">
      <div class="mark"></div>
      <span>Harbour Crafted</span>
    </div>

    <p class="tagline">Designed by an Australian plumber</p>

    <div class="brand">
      <div class="mark"></div>
      <div class="brand-name">TWIST HOOK</div>
      <div class="brand-sub">Silicone Nozzles</div>
    </div>
  </section>
</main>
</body>
</html>
```